Seasonal Postcard - Branding Campaign for Mechanical Company

Postcard branding campaign. Image size must be 2775x1875 pixels landscape only. JPEG or PNG format. Cannot exceed 10MB. Looking for multiple designs for different monthly postcards to send to existing customer 2x a month. Go to www.brightforgeservicesnc.com for color schemes and design feel. Seasonal postcard for Spring, Summer, Fall and Winter Feel for promoting our residential plumbing, electrical, heating and cooling(HVAC) and generator repair and maintenance services. Clean, non cluttered design. You can design to include all services, or just target one service and one season. Some coupons can be offered for each department (HVAC - $49 Off HVAC Check Up) (Generator - $300 Off Generator Installation) (Electrical - Free Electrical Panel Inspection) (Plumbing - $50 Off Water Heater Installation)

Target Market(s)

Homeowners age 35+

Colors

Designer to choose colors to be used in the design.

Requirements
Should not have
• any phone numbers (please photoshop off of any images of vehicles)

```html
<!DOCTYPE html>
<html lang="en">
<head>
<meta charset="utf-8">
<title>Brightforge Services – Seasonal Postcards</title>
<link href="https://fonts.googleapis.com/css2?family=Oswald:wght@500;700&family=Roboto+Condensed:wght@300;400&family=Montserrat:wght@800&display=swap" rel="stylesheet">
<style>
  :root{
    --board:#2b2b2b;
    --navy:#22408e;
    --brand-red:#e5262c;
    --white:#ffffff;
    --badge:#c9ccd3;
    --badge-dark:#8d93a1;
  }
  *{box-sizing:border-box;margin:0;padding:0}
  html,body{width:1200px;height:1200px;overflow:hidden;background:var(--board)}
  .board{position:relative;width:1200px;height:1200px}

  .postcard{position:absolute;width:508px;height:342px;background:var(--white);overflow:hidden}
  .postcard--summer{left:71px;top:144px}
  .postcard--spring{left:629px;top:145px}
  .postcard--winter{left:71px;top:711px;width:514px;height:347px}
  .postcard--fall{left:622px;top:711px;width:515px;height:348px}

  .brand{position:absolute;right:22px;top:22px;display:flex;align-items:center;gap:8px;
    font-family:"Oswald",sans-serif;font-weight:700;font-size:27px;letter-spacing:1px;color:var(--navy);line-height:1}
  .brand__mark{width:18px;height:18px;background:var(--navy)}

  .service-band{position:absolute;left:0;right:0;top:23%;height:17.5%;background:var(--navy);
    display:flex;align-items:center;justify-content:flex-end;padding-right:18px;
    font-family:"Montserrat",sans-serif;font-weight:800;font-size:23px;color:var(--white);white-space:nowrap}
  .offer-panel{position:absolute;left:0;right:0;top:40.5%;height:41%;background:var(--brand-red)}
  .offer-box{position:absolute;left:54%;width:33%;top:9%;height:60%;
    border-top:1px dashed rgba(255,255,255,.75);border-bottom:1px dashed rgba(255,255,255,.75);
    display:flex;flex-direction:column;align-items:center;justify-content:center;color:var(--white);text-align:center}
  .offer-box::before,.offer-box::after{content:"";position:absolute;top:8%;bottom:8%;border-left:1px dashed rgba(255,255,255,.75)}
  .offer-box::before{left:0}.offer-box::after{right:0}
  .offer-box__amount{font-family:"Oswald",sans-serif;font-weight:700;font-size:40px;line-height:1.05}
  .offer-box__detail{font-family:"Roboto Condensed",sans-serif;font-weight:300;font-size:14px;white-space:nowrap}
  .offer-panel__urgency{position:absolute;left:54%;width:33%;top:79%;text-align:center;
    font-family:"Roboto Condensed",sans-serif;font-weight:300;font-size:15px;color:var(--white);white-space:nowrap}

  .partner-strip{position:absolute;left:50%;right:2%;bottom:3%;height:14%;
    display:grid;grid-template-columns:repeat(5,1fr);grid-template-rows:1fr 1fr;gap:4px 10px;align-items:center;justify-items:center}
  .partner-badge{width:22px;height:14px;border-radius:3px;background:var(--badge)}
  .partner-badge--wide{width:44px;height:12px;border-radius:2px}
  .partner-badge--round{width:16px;height:16px;border-radius:50%;background:var(--badge-dark)}

  .season-photo{position:absolute;left:-145px;top:84px;width:410px;height:410px;border-radius:50%;
    border:6px solid var(--white);z-index:2}
  .postcard--summer .season-photo{background:radial-gradient(circle at 40% 25%,#f6a57a,#d9476b 45%,#f0f0f2 62%,#c8c8cc)}
  .postcard--spring .season-photo{background:radial-gradient(circle at 45% 20%,#e2472c,#6b8f3a 35%,#c6c8c6 55%,#8f918f)}
  .postcard--winter .season-photo{background:linear-gradient(160deg,#f2f2f2,#d8d9dc 40%,#4c4f5a 70%,#eeeeee)}
  .postcard--fall .season-photo{background:radial-gradient(circle at 55% 55%,#2f5fa8,#8b8f97 40%,#ededed 60%,#dcdcdc)}

  .season-label{position:absolute;font-family:"Oswald",sans-serif;font-weight:700;font-size:40px;color:var(--white);
    transform:translateX(-50%);letter-spacing:.5px}
</style>
</head>
<body>
<main class="board">

  <article class="postcard postcard--summer">
    <div class="brand"><span class="brand__mark"></span>BRIGHTFORGE SERVICES</div>
    <div class="service-band">Generator Installation</div>
    <div class="offer-panel">
      <div class="offer-box"><div class="offer-box__amount">$300 OFF</div><div class="offer-box__detail">on generator Installation</div></div>
      <div class="offer-panel__urgency">Limited offer ! Hurry Up!</div>
    </div>
    <div class="partner-strip">
      <span class="partner-badge"></span><span class="partner-badge--round partner-badge"></span><span class="partner-badge partner-badge--wide"></span><span class="partner-badge partner-badge--wide"></span><span class="partner-badge--round partner-badge"></span>
      <span class="partner-badge"></span><span class="partner-badge"></span><span class="partner-badge partner-badge--wide"></span><span class="partner-badge--round partner-badge"></span><span class="partner-badge"></span>
    </div>
    <div class="season-photo" role="img" aria-label="Home standby generator in front of palm trees at sunset"></div>
  </article>

  <article class="postcard postcard--spring">
    <div class="brand"><span class="brand__mark"></span>BRIGHTFORGE SERVICES</div>
    <div class="service-band">HVAC Check Up</div>
    <div class="offer-panel">
      <div class="offer-box"><div class="offer-box__amount">$49 OFF</div><div class="offer-box__detail">on HVAC Check Up</div></div>
      <div class="offer-panel__urgency">Limited offer ! Hurry Up!</div>
    </div>
    <div class="partner-strip">
      <span class="partner-badge"></span><span class="partner-badge--round partner-badge"></span><span class="partner-badge partner-badge--wide"></span><span class="partner-badge partner-badge--wide"></span><span class="partner-badge--round partner-badge"></span>
      <span class="partner-badge"></span><span class="partner-badge"></span><span class="partner-badge partner-badge--wide"></span><span class="partner-badge--round partner-badge"></span><span class="partner-badge"></span>
    </div>
    <div class="season-photo" role="img" aria-label="Outdoor air conditioning unit among red spring poppies"></div>
  </article>

  <article class="postcard postcard--winter">
    <div class="brand"><span class="brand__mark"></span>BRIGHTFORGE SERVICES</div>
    <div class="service-band">Water Heater Installation</div>
    <div class="offer-panel">
      <div class="offer-box"><div class="offer-box__amount">$50 OFF</div><div class="offer-box__detail">on Water Heater Installation</div></div>
      <div class="offer-panel__urgency">Limited offer ! Hurry Up!</div>
    </div>
    <div class="partner-strip">
      <span class="partner-badge"></span><span class="partner-badge--round partner-badge"></span><span class="partner-badge partner-badge--wide"></span><span class="partner-badge partner-badge--wide"></span><span class="partner-badge--round partner-badge"></span>
      <span class="partner-badge"></span><span class="partner-badge"></span><span class="partner-badge partner-badge--wide"></span><span class="partner-badge--round partner-badge"></span><span class="partner-badge"></span>
    </div>
    <div class="season-photo" role="img" aria-label="Children in snowsuits standing in snow beside a service van"></div>
  </article>

  <article class="postcard postcard--fall">
    <div class="brand"><span class="brand__mark"></span>BRIGHTFORGE SERVICES</div>
    <div class="service-band">Electrical Panel Inspection</div>
    <div class="offer-panel">
      <div class="offer-box"><div class="offer-box__amount">FREE</div><div class="offer-box__detail">Electrical Panel Inspection</div></div>
      <div class="offer-panel__urgency">Limited offer ! Hurry Up!</div>
    </div>
    <div class="partner-strip">
      <span class="partner-badge"></span><span class="partner-badge--round partner-badge"></span><span class="partner-badge partner-badge--wide"></span><span class="partner-badge partner-badge--wide"></span><span class="partner-badge--round partner-badge"></span>
      <span class="partner-badge"></span><span class="partner-badge"></span><span class="partner-badge partner-badge--wide"></span><span class="partner-badge--round partner-badge"></span><span class="partner-badge"></span>
    </div>
    <div class="season-photo" role="img" aria-label="Hand adjusting a wall touchscreen thermostat with autumn leaves"></div>
  </article>

  <div class="season-label" style="left:321px;top:516px">SUMMER</div>
  <div class="season-label" style="left:865px;top:516px">SPRING</div>
  <div class="season-label" style="left:283px;top:1088px">WINTER</div>
  <div class="season-label" style="left:908px;top:1088px">FALL</div>

</main>
</body>
</html>
```